Educational website design and repeat learning

The aim of the project is to create a learning platform to support high school students in their learning. It aims to integrate as much as possible the potential of digital tools (videos, navigation) in the educational path of students, in the acquisition of knowledge and its use. In particular, it will integrate a learning system in spaced repetition (flashcards).

The students are the central users of the platform. They must have access to the following features:
• Access to course content and the map review tool
• Personal dashboard, retracing the courses taken, the number of revised cards and other metrics
• A notification panel, suggesting to him the revision of such or such pack of cards, or of such or such concept in the rest of the contents

Flashcards are a learning system based on spaced repetition, on a format of cards associating a question and an answer. Ideally, each card involves only a limited amount of knowledge. The learner successively repeats the cards and associates with each of them a difficulty (or failure if necessary), leading the system to offer him, as a priority, the cards that are the most difficult for him.

Once the designer has been chosen, the site map and the wireframes will be transmitted to start work on the site code.
Updates

Les designs se ressemblent

Target Market(s)

High school students - France

Industry/Entity Type

Education

Logo Text

lumo-stacks

Coding

Coded - Design and coding required

Number of Pages Required

4 page

Font styles to use
Sans Serif

Requirements
Must have
• Must be offered:
- 1 design of home page, content (lorem ipsum), possibility of connection / registration
- 1 course sheet page design, with the complete course hierarchy
- 1 design of the spaced repetition tool
Nice to have
• - 1 student dashboard design with the following elements:
• Time spent on the platform (graph week by week + week in progress)
• Number of course sheets read (total and week)
• Number of cards revised (total and week)
Should not have
• Light blue

```html
<!DOCTYPE html>
<html lang="en">
<head>
<meta charset="utf-8">
<title>lumo-stacks — knowledge is power</title>
<link href="https://fonts.googleapis.com/css2?family=Montserrat:wght@400;500;600;700&family=Nunito:wght@400;600;700&display=swap" rel="stylesheet">
<style>
:root{
  --green:#2aa75a;
  --green-dark:#23924d;
  --mint:#2ed18c;
  --ink:#1f1f1f;
  --text:#333;
  --muted:#6b6b6b;
  --grey-bg:#efefef;
  --card-bg:#f1f1f1;
  --white:#fff;
  --footer:#3b3f43;
  --footer-text:#c9cccf;
  --hero-a:#3d2b22;
  --hero-b:#24180f;
  --deck-a:#2f7d54;
  --deck-b:#8fc9a3;
  --deck-c:#d98fc9;
}
*{box-sizing:border-box;margin:0;padding:0}
html,body{width:1200px;height:4216px;overflow:hidden}
body{position:relative;font-family:'Nunito',sans-serif;color:var(--text);background:var(--white)}
.abs{position:absolute}

/* hero */
.hero{position:absolute;left:0;top:0;width:1200px;height:583px;background:linear-gradient(160deg,var(--hero-a),var(--hero-b) 60%,#2e2019)}
.hero-photo{position:absolute;inset:0;background:radial-gradient(ellipse at 20% 10%,rgba(120,100,85,.35),transparent 45%),radial-gradient(ellipse at 88% 12%,rgba(150,150,150,.25),transparent 30%)}
.brand{position:absolute;display:flex;align-items:center;gap:8px;font-family:'Montserrat',sans-serif;font-weight:700;color:var(--white);white-space:nowrap}
.brand-mark{width:14px;height:14px;background:var(--green)}
.hero .brand{left:84px;top:64px;font-size:22px}
.nav{position:absolute;left:355px;top:67px;display:flex;gap:39px;font-family:'Montserrat',sans-serif;font-size:9.5px;font-weight:600;letter-spacing:1px;color:var(--white);white-space:nowrap}
.btn-login{position:absolute;left:905px;top:60px;width:97px;height:28px;border:1.5px solid var(--green);border-radius:3px;color:var(--green);font:600 9.5px 'Montserrat',sans-serif;display:flex;align-items:center;justify-content:center;letter-spacing:.5px}
.btn-register{position:absolute;left:1015px;top:60px;width:97px;height:28px;background:var(--green);border-radius:3px;color:var(--white);font:600 9.5px 'Montserrat',sans-serif;display:flex;align-items:center;justify-content:center;letter-spacing:1px}
.hero-title{position:absolute;left:0;width:1212px;top:216px;text-align:center;font:600 46px 'Nunito',sans-serif;letter-spacing:4px;color:var(--white)}
.hero-sub{position:absolute;left:0;width:1212px;top:280px;text-align:center;font:400 23px 'Nunito',sans-serif;letter-spacing:2px;color:var(--white)}
.btn-start{position:absolute;left:511px;top:347px;width:222px;height:57px;background:var(--green);border-radius:3px;color:var(--white);font:700 14px 'Montserrat',sans-serif;letter-spacing:3px;display:flex;align-items:center;justify-content:center}

/* stats */
.stats{position:absolute;left:0;top:583px;width:1200px;height:205px;background:var(--white)}
.stat-text{position:absolute;font:400 20px/1.2 'Nunito',sans-serif;color:#444;white-space:nowrap}
.stat-text b{font-weight:700}
.stats-rule{position:absolute;left:126px;top:203px;width:935px;height:2px;background:#e7e7e7}

/* features */
.features{position:absolute;left:0;top:788px;width:1200px;height:946px;background:var(--grey-bg)}
.section-title{position:absolute;left:0;width:1200px;text-align:center;font:500 28px 'Nunito',sans-serif;color:var(--ink)}
.feature{position:absolute;width:220px;text-align:center}
.feature-icon{width:106px;height:106px;margin:0 auto;border-radius:50%;background:var(--white);display:flex;align-items:center;justify-content:center}
.feature h3{margin-top:14px;font:600 18px 'Nunito',sans-serif;color:var(--ink);white-space:nowrap}
.feature p{width:200px;margin:6px auto 0;font:400 11.3px/1.3 'Nunito',sans-serif;color:#444}

/* subjects band */
.subjects{position:absolute;left:0;top:1734px;width:1200px;height:525px;background:linear-gradient(120deg,#6f6f6f,#4d4d4d 40%,#5e5a57 70%,#3c3c3c)}
.laptop{position:absolute;left:344px;top:1676px;width:535px;height:362px;background:#f8f8f8;border:2px solid #e2e2e2;border-radius:14px 14px 0 0}
.laptop-screen{position:absolute;left:352px;top:1684px;width:519px;height:326px;background:linear-gradient(100deg,#b9b3a9,#d8d1c6 45%,#c9b9a8 70%,#a9a29a)}
.laptop-base{position:absolute;left:283px;top:2038px;width:658px;height:17px;background:linear-gradient(#f1f1f1,#cfcfcf);border-radius:0 0 60px 60px/0 0 14px 14px}
.laptop-notch{position:absolute;left:566px;top:2038px;width:92px;height:5px;background:#bdbdbd;border-radius:0 0 6px 6px}
.play{position:absolute;left:552px;top:1804px}
.tag{position:absolute;height:30px;border:1.5px solid var(--green);border-radius:3px;color:var(--white);font:700 10px 'Montserrat',sans-serif;letter-spacing:1.5px;display:flex;align-items:center;justify-content:center;background:rgba(0,0,0,.08);white-space:nowrap}

/* courses */
.course{position:absolute;top:2405px;width:233px;height:484px;background:var(--card-bg)}
.course-img{height:188px}
.course h3{position:absolute;left:20px;top:208px;font:600 18px 'Nunito',sans-serif;color:var(--ink);white-space:nowrap}
.course p{position:absolute;left:20px;top:245px;width:200px;font:400 11.3px/1.3 'Nunito',sans-serif;color:#444}
.course .divider{position:absolute;left:0;top:306px;width:233px;height:2px;background:#d9d9d9}
.course .meta{position:absolute;left:30px;width:173px;text-align:center;font:400 14.5px 'Nunito',sans-serif;color:#222;border-bottom:1.5px solid #d6d6d6;padding-bottom:8px;white-space:nowrap}
.course .join{position:absolute;left:15px;top:435px;width:203px;height:36px;background:var(--green);border-radius:18px;color:var(--white);font:700 14px 'Nunito',sans-serif;display:flex;align-items:center;justify-content:center}
.view-all{position:absolute;left:0;width:1212px;top:2928px;text-align:center;font:400 14px 'Nunito',sans-serif;color:#666}

/* tutor */
.tutor-title{position:absolute;left:0;width:1200px;top:3030px;text-align:center;font:500 25px 'Montserrat',sans-serif;color:var(--ink)}
.avatar{position:absolute;left:537px;top:3099px;width:124px;height:124px;border-radius:50%;background:radial-gradient(circle at 50% 40%,#9a8f88,#4b4f52 70%)}
.tutor-note{position:absolute;left:0;width:1208px;top:3251px;text-align:center;font:400 14px 'Nunito',sans-serif;color:#555}
.audio{position:absolute;left:495px;top:3283px;display:flex;align-items:center;gap:10px;font:400 10px 'Nunito',sans-serif;color:#999}
.audio .bar{width:90px;height:2px;background:#ccc}

/* register */
.video{position:absolute;left:124px;top:3479px;width:413px;height:270px;background:linear-gradient(90deg,var(--deck-a) 0%,var(--deck-b) 50%,var(--deck-c) 50%,#c77bb8 100%)}
.video-shadow{position:absolute;left:110px;top:3745px;width:440px;height:36px;background:radial-gradient(ellipse at center,rgba(0,0,0,.22),transparent 70%)}
.register-card{position:absolute;left:627px;top:3421px;width:485px;height:369px;background:var(--white);box-shadow:0 2px 14px rgba(0,0,0,.1)}
.register-card h2{position:absolute;left:0;width:485px;top:31px;text-align:center;font:700 17px 'Nunito',sans-serif;color:var(--ink)}
.field{position:absolute;left:26px;width:432px;height:42px;background:#f0f0f0;border-radius:3px;padding-left:19px;display:flex;align-items:center;font:400 17px 'Nunito',sans-serif;color:#a9a9a9;letter-spacing:1px}
.btn-submit{position:absolute;left:26px;top:282px;width:432px;height:60px;background:var(--mint);border-radius:3px;color:var(--white);font:700 16px 'Montserrat',sans-serif;letter-spacing:4px;display:flex;align-items:center;justify-content:center}

/* footer */
.footer{position:absolute;left:0;top:3898px;width:1200px;height:266px;background:var(--footer)}
.footer-col{position:absolute;top:70px;font:400 13px/21px 'Nunito',sans-serif;color:var(--footer-text);letter-spacing:.5px}
.footer-col .head{color:#8e9295}
.footer-rule{position:absolute;left:818px;top:47px;width:1px;height:205px;background:#5a5f63}
.footer .brand{right:88px;top:72px;font-size:24px}
.contact{position:absolute;right:88px;top:120px;text-align:right;font:400 12px/20px 'Nunito',sans-serif;color:var(--footer-text)}
.contact .head{color:#8e9295;font-size:11px}
.socials{position:absolute;right:92px;top:205px;display:flex;gap:14px}
.socials span{width:11px;height:11px;border-radius:50%;background:var(--white)}
.bottom-bar{position:absolute;left:0;top:4164px;width:1200px;height:52px;background:var(--green);font:600 10.5px 'Nunito',sans-serif;color:var(--white)}
.bottom-bar span{position:absolute;top:20px}
</style>
</head>
<body>

<header class="hero">
  <div class="hero-photo" role="img" aria-label="Desk top with laptop, tablet and clipboard, darkened"></div>
  <div class="brand"><span class="brand-mark"></span>lumo-stacks</div>
  <nav class="nav"><span>HOW IT WORKS</span><span>SUBJECT</span><span>PRICES</span><span>CONTACT US</span><span>INFORMATION</span></nav>
  <a class="btn-login">Log-in</a>
  <a class="btn-register">REGISTER</a>
  <h1 class="hero-title">knowledge is power</h1>
  <p class="hero-sub">improving student learning</p>
  <a class="btn-start">GET STARTED</a>
</header>

<section class="stats">
  <svg class="abs" style="left:205px;top:52px" width="90" height="90" viewBox="0 0 90 90"><circle cx="45" cy="45" r="42" fill="none" stroke="var(--green)" stroke-width="5"/><path d="M26 46 L40 59 L65 32" fill="none" stroke="var(--green)" stroke-width="5" stroke-linecap="round" stroke-linejoin="round"/></svg>
  <p class="stat-text" style="left:316px;top:62px">Over <b>500</b><br>Flashcard decks ready.<br>A deck for every topic.</p>
  <svg class="abs" style="left:727px;top:52px" width="94" height="92" viewBox="0 0 94 92" fill="none" stroke="var(--green)" stroke-width="3" stroke-linejoin="round">
    <circle cx="20" cy="14" r="9"/><circle cx="47" cy="14" r="9"/><circle cx="74" cy="14" r="9"/>
    <path d="M4 44 V36 Q4 26 20 26 Q36 26 36 36 V44"/><path d="M31 44 V36 Q31 26 47 26 Q63 26 63 36 V44"/><path d="M58 44 V36 Q58 26 74 26 Q90 26 90 36 V44"/>
    <path d="M16 52 l4 8 9 1 -7 6 2 9 -8 -5 -8 5 2 -9 -7 -6 9 -1z"/>
    <path d="M47 60 l4 8 9 1 -7 6 2 9 -8 -5 -8 5 2 -9 -7 -6 9 -1z"/>
    <path d="M78 52 l4 8 9 1 -7 6 2 9 -8 -5 -8 5 2 -9 -7 -6 9 -1z"/>
  </svg>
  <p class="stat-text" style="left:841px;top:62px">Over 1.5 million<br>cards revised by<br>students</p>
  <div class="stats-rule"></div>
</section>

<section class="features">
  <h2 class="section-title" style="top:176px">Features</h2>

  <div class="feature" style="left:240px;top:305px">
    <div class="feature-icon"><svg width="44" height="54" viewBox="0 0 44 54" fill="none" stroke="var(--green)" stroke-width="2"><rect x="2" y="2" width="40" height="50"/><rect x="8" y="9" width="8" height="8"/><rect x="8" y="23" width="8" height="8"/><rect x="8" y="37" width="8" height="8"/><path d="M21 13h15M21 27h15M21 41h15"/></svg></div>
    <h3>Course Sheets</h3><p>Lorem ipsum dolor sit amet, consectetur adipisicing elit, sed do eiusmod tempor incididunt ut labore et dolore magna.</p>
  </div>
  <div class="feature" style="left:491px;top:305px">
    <div class="feature-icon"><svg width="40" height="54" viewBox="0 0 40 54" fill="none" stroke="var(--green)" stroke-width="2"><circle cx="20" cy="16" r="11"/><path d="M4 52 V42 Q4 32 20 32 Q36 32 36 42 V52Z"/><path d="M20 32 V52"/></svg></div>
    <h3>Personal Dashboard</h3><p>Lorem ipsum dolor sit amet, consectetur adipisicing elit, sed do eiusmod tempor incididunt ut labore et dolore magna.</p>
  </div>
  <div class="feature" style="left:741px;top:305px">
    <div class="feature-icon"><svg width="40" height="56" viewBox="0 0 40 56" fill="none" stroke="var(--green)" stroke-width="2"><circle cx="20" cy="18" r="16"/><circle cx="20" cy="18" r="9"/><path d="M11 31 L9 52 L20 45 L31 52 L29 31"/></svg></div>
    <h3>Revision Alerts</h3><p>Lorem ipsum dolor sit amet, consectetur adipisicing elit, sed do eiusmod tempor incididunt ut labore et dolore magna.</p>
  </div>

  <div class="feature" style="left:240px;top:554px">
    <div class="feature-icon"><svg width="56" height="56" viewBox="0 0 56 56" fill="none" stroke="var(--green)" stroke-width="2"><ellipse cx="28" cy="28" rx="25" ry="10"/><ellipse cx="28" cy="28" rx="25" ry="10" transform="rotate(60 28 28)"/><ellipse cx="28" cy="28" rx="25" ry="10" transform="rotate(-60 28 28)"/><circle cx="28" cy="28" r="4" fill="var(--green)"/></svg></div>
    <h3>Spaced Repetition</h3><p>Lorem ipsum dolor sit amet, consectetur adipisicing elit, sed do eiusmod tempor incididunt ut labore et dolore magna.</p>
  </div>
  <div class="feature" style="left:491px;top:554px">
    <div class="feature-icon"><svg width="54" height="40" viewBox="0 0 54 40" fill="none" stroke="var(--green)" stroke-width="2"><rect x="2" y="2" width="50" height="32"/><rect x="7" y="7" width="40" height="22"/><path d="M14 24 L24 18 L30 22 L38 14 M10 38h34"/></svg></div>
    <h3>Video Lessons</h3><p>Lorem ipsum dolor sit amet, consectetur adipisicing elit, sed do eiusmod tempor incididunt ut labore et dolore magna.</p>
  </div>
  <div class="feature" style="left:741px;top:554px">
    <div class="feature-icon"><svg width="40" height="54" viewBox="0 0 40 54" fill="none" stroke="var(--green)" stroke-width="2"><rect x="2" y="2" width="36" height="50"/><path d="M9 2 V52"/><rect x="16" y="10" width="15" height="12"/></svg></div>
    <h3>Flashcards</h3><p>Lorem ipsum dolor sit amet, consectetur adipisicing elit, sed do eiusmod tempor incididunt ut labore et dolore magna.</p>
  </div>
</section>

<section class="subjects" role="img" aria-label="Blurred classroom photograph behind the subject list"></section>
<div class="laptop"></div>
<div class="laptop-screen" role="img" aria-label="Video still of a teacher holding folders in a classroom"></div>
<div class="laptop-base"></div>
<div class="laptop-notch"></div>
<svg class="play" width="124" height="124" viewBox="0 0 124 124"><circle cx="62" cy="62" r="60" fill="rgba(40,40,40,.55)"/><circle cx="62" cy="62" r="52" fill="none" stroke="var(--green)" stroke-width="4" stroke-dasharray="250 80"/><path d="M50 40 L82 62 L50 84Z" fill="none" stroke="var(--green)" stroke-width="4" stroke-linejoin="round"/></svg>

<div class="tag" style="left:295px;top:2128px;width:78px">MATHS</div>
<div class="tag" style="left:388px;top:2128px;width:113px">CHEMISTRY</div>
<div class="tag" style="left:514px;top:2128px;width:92px">BIOLOGY</div>
<div class="tag" style="left:620px;top:2128px;width:92px">PHYSICS</div>
<div class="tag" style="left:727px;top:2128px;width:178px">COMPUTER SCIENCE</div>
<div class="tag" style="left:296px;top:2167px;width:187px">ENGLISH LITERATURE</div>
<div class="tag" style="left:498px;top:2167px;width:93px">FRENCH</div>
<div class="tag" style="left:606px;top:2167px;width:122px">ACCOUNTING</div>
<div class="tag" style="left:745px;top:2167px;width:157px">OTHER SUBJECTS</div>

<h2 class="section-title" style="top:2340px">Courses</h2>

<article class="course" style="left:232px">
  <div class="course-img" role="img" aria-label="Hands typing on a laptop on a wooden desk" style="background:linear-gradient(135deg,#5a3d2a,#3a2a20 60%,#6b5040)"></div>
  <h3>Mathematics</h3>
  <p>Lorem ipsum dolor sit amet, consectetur adipisicing elit, sed do eiusmod tempor.</p>
  <div class="divider"></div>
  <div class="meta" style="top:324px">Time : 3 pm</div>
  <div class="meta" style="top:362px">Teacher: Mara Lind</div>
  <a class="join">Join Now</a>
</article>
<article class="course" style="left:483px">
  <div class="course-img" role="img" aria-label="Camera resting beside a student asleep on a desk" style="background:linear-gradient(135deg,#7a1f22,#c9a58f 55%,#3a3a3a)"></div>
  <h3>Physics</h3>
  <p>Lorem ipsum dolor sit amet, consectetur adipisicing elit, sed do eiusmod tempor.</p>
  <div class="divider"></div>
  <div class="meta" style="top:324px">Time : 6 pm</div>
  <div class="meta" style="top:362px">Teacher: Theo Marin</div>
  <a class="join">Join Now</a>
</article>
<article class="course" style="left:733px">
  <div class="course-img" role="img" aria-label="Wrist with a smartwatch, checking revision time" style="background:linear-gradient(135deg,#1f5c3f,#3f8f63 55%,#24493a)"></div>
  <h3>History</h3>
  <p>Lorem ipsum dolor sit amet, consectetur adipisicing elit, sed do eiusmod tempor.</p>
  <div class="divider"></div>
  <div class="meta" style="top:324px">Time : 10 am</div>
  <div class="meta" style="top:362px">Teacher: Inès Duval</div>
  <a class="join">Join Now</a>
</article>

<p class="view-all">View all</p>

<h2 class="tutor-title">TUTOR QUALIFICATION &amp; EXPERIENCE</h2>
<svg class="abs" style="left:416px;top:3151px" width="16" height="20" viewBox="0 0 16 20"><path d="M12 2 L4 10 L12 18" fill="none" stroke="#555" stroke-width="2.5"/></svg>
<div class="avatar" role="img" aria-label="Portrait photograph of the tutor"></div>
<svg class="abs" style="left:752px;top:3151px" width="16" height="20" viewBox="0 0 16 20"><path d="M4 2 L12 10 L4 18" fill="none" stroke="#555" stroke-width="2.5"/></svg>
<p class="tutor-note">Hello - Have a listen to my tutor profile.</p>
<div class="audio"><span>▶</span><span>0:00 / 0:00</span><span class="bar"></span><span>◀</span></div>

<div class="video-shadow"></div>
<div class="video" role="img" aria-label="Cartoon video thumbnail of two students revising at desks"></div>

<section class="register-card">
  <h2>Register Now</h2>
  <div class="field" style="top:76px">Name</div>
  <div class="field" style="top:138px">Phone Number</div>
  <div class="field" style="top:202px">E-mail</div>
  <a class="btn-submit">REGISTER</a>
</section>

<footer class="footer">
  <div class="footer-col" style="left:88px"><span class="head">Information</span><br>About Us<br>Become a Tutor<br>Testimonial &amp;<br>Reviews</div>
  <div class="footer-col" style="left:345px;top:91px">Flashcard decks<br>Course sheets<br>Revision planner<br>Helpful Links</div>
  <div class="footer-col" style="left:594px;top:91px">Schools<br>Staying safe online<br>Schools</div>
  <div class="footer-rule"></div>
  <div class="brand"><span class="brand-mark"></span>lumo-stacks</div>
  <div class="contact"><span class="head">Contact Us</span><br>+11 (0) 200 555 0147<br>hello@lumo-stacks.com</div>
  <div class="socials"><span></span><span></span><span></span><span></span></div>
</footer>
<div class="bottom-bar">
  <span style="left:88px">Sitemap</span>
  <span style="left:172px">Privacy Policy</span>
  <span style="left:288px">Trust &amp; Security</span>
  <span style="right:88px">Copyright © 2018, lumo-stacks</span>
</div>

</body>
</html>
```